Create a Graphic About YOURSELF and PixelHarbor

PixelHarbor would like you (designers) to create an awesome graphic to promote YOURSELF and your profile on PixelHarbor!

Your graphic should communicate your name, your services and should mention PixelHarbor.

The design should be perfect for sharing on Chatterly. Here's an example of what we'd like http://blog.pixelharbor-example.ca/article/333/pixelharbor-launches-3000-hire-me-social-design-contest

Once you submitted your design, we'd love you to share the design ('advertisement') and promote yourself and PixelHarbor to your friends and potential customers. So make your submissions great and get your friends to vote for your design by 'Liking' it on Chatterly!

Prizes:
$1500 - "PixelHarbor Community" prize awarded to the designer with the most Chatterly 'Likes'
5 x $50 for the next 5 'most liked' designs on Chatterly

$1000 - "Hire Me" prize awarded to the designer who receives the most client invites
5 x $50 for the next 5 'most invited' designers

In summary, this is a great opportunity for you to increase your exposure to PixelHarbor customers and win cash prizes. Show off your design skills and get hired by PixelHarbor customers from around the world!

Target Market(s)

Fans, friends and customers of YOU

Industry/Entity Type

Cash

Requirements
Must have
• 1) Include your PixelHarbor user name on the graphic so customers can find you in the PixelHarbor Designer Directory
2) Include the tagline "Hire Me on PixelHarbor.com!" in your graphic design.
3) Share your design's URL on our Chatterly wall at http://chatterly-example.com/pixelharbor and get your friends to 'like' your design.
Nice to have
• 1) Include a tagline that expresses your design approach/philosophy
2) Artwork dimensions: 403 x 403 px
3) You can submit more than 1 design!
Should not have
• You must own the copyright of any images you use including stock imagery.

```html
<!DOCTYPE html>
<html lang="en">
<head>
<meta charset="utf-8">
<title>Karim Aldane – Graphic Designer</title>
<link rel="stylesheet" href="https://fonts.googleapis.com/css2?family=Audiowide&family=Pinyon+Script&family=Patrick+Hand&family=Open+Sans:wght@600&display=swap">
<style>
  :root {
    --sky-light: #3fa6e6;
    --sky-mid: #1f86cf;
    --sky-deep: #0f5fa6;
    --glow: #8fd3ff;
    --ink: #10253d;
    --script-ink: #1b2230;
    --badge-orange: #f07a12;
    --badge-shade: #b8500a;
    --paper: #ffffff;
    --brand-navy: #16324f;
  }
  * { box-sizing: border-box; margin: 0; padding: 0; }
  html, body { width: 1200px; height: 1200px; overflow: hidden; }
  body { background: var(--paper); }

  .promo {
    position: relative;
    width: 1200px;
    height: 1200px;
    overflow: hidden;
  }

  .promo__stage {
    position: absolute;
    left: 0; top: 0;
    width: 1200px; height: 1020px;
    background:
      radial-gradient(ellipse 70% 45% at 50% 38%, rgba(140,210,255,0.55), rgba(140,210,255,0) 70%),
      linear-gradient(180deg, var(--sky-mid) 0%, var(--sky-light) 40%, var(--sky-mid) 75%, var(--sky-deep) 100%);
    overflow: hidden;
  }

  .service-tag {
    position: absolute;
    font-family: "Patrick Hand", cursive;
    font-size: 58px;
    color: rgba(255,255,255,0.16);
    white-space: nowrap;
  }

  .promo__name {
    position: absolute;
    left: 0; right: 0; top: 300px;
    text-align: center;
    font-family: "Audiowide", sans-serif;
    font-size: 112px;
    color: #ffffff;
    letter-spacing: 2px;
    text-shadow: 0 0 14px var(--glow), 0 0 30px rgba(120,200,255,0.8), 0 0 4px #ffffff;
  }

  .promo__role {
    position: absolute;
    left: 0; right: 0; top: 410px;
    text-align: center;
    font-family: "Pinyon Script", cursive;
    font-size: 104px;
    color: var(--script-ink);
  }

  .hire-badge {
    position: absolute;
    left: 470px; top: 855px;
    width: 250px; height: 160px;
  }
  .hire-badge__label {
    position: absolute;
    left: 58px; top: 20px;
    width: 160px;
    text-align: center;
    font-family: "Audiowide", sans-serif;
    font-size: 32px;
    line-height: 42px;
    color: #ffffff;
    transform: rotate(-7deg);
  }

  .promo__footer {
    position: absolute;
    left: 0; top: 1020px;
    width: 1200px; height: 180px;
    background: var(--paper);
    display: flex;
    align-items: center;
    padding-left: 112px;
    gap: 36px;
  }
  .brand-dot {
    width: 140px; height: 140px;
    border-radius: 50%;
    background: var(--brand-navy);
    flex: none;
  }
  .brand-name {
    font-family: "Open Sans", sans-serif;
    font-weight: 600;
    font-size: 118px;
    letter-spacing: -2px;
    color: var(--brand-navy);
    line-height: 1;
  }
</style>
</head>
<body>
<main class="promo">
  <section class="promo__stage">
    <span class="service-tag" style="left:100px;top:150px;transform:rotate(-25deg)">Flyer</span>
    <span class="service-tag" style="left:570px;top:80px;transform:rotate(10deg)">Business Card</span>
    <span class="service-tag" style="left:200px;top:210px;transform:rotate(-10deg)">Logo</span>
    <span class="service-tag" style="left:470px;top:210px;transform:rotate(-8deg)">Poster</span>
    <span class="service-tag" style="left:950px;top:190px;transform:rotate(-12deg)">Brochur</span>
    <span class="service-tag" style="left:990px;top:470px;transform:rotate(30deg)">Flyer</span>
    <span class="service-tag" style="left:20px;top:470px;transform:rotate(-15deg)">Logo</span>
    <span class="service-tag" style="left:280px;top:590px;transform:rotate(-20deg)">Brochur</span>
    <span class="service-tag" style="left:530px;top:640px;transform:rotate(-10deg)">Logo</span>
    <span class="service-tag" style="left:880px;top:570px;transform:rotate(-8deg)">Brochur</span>
    <span class="service-tag" style="left:-60px;top:700px;transform:rotate(-20deg)">Business Card</span>
    <span class="service-tag" style="left:620px;top:740px;transform:rotate(-15deg)">Poster</span>
    <span class="service-tag" style="left:880px;top:720px;transform:rotate(10deg)">Business Card</span>
    <span class="service-tag" style="left:120px;top:820px;transform:rotate(-20deg)">Flyer</span>

    <h1 class="promo__name">Karim Aldane</h1>
    <p class="promo__role">Graphic Designer</p>

    <div class="hire-badge">
      <svg width="250" height="160" viewBox="0 0 250 160" aria-hidden="true">
        <path d="M40 118 L18 150 L70 128 Z" fill="var(--badge-shade)"/>
        <path d="M30 34 Q28 14 50 12 L200 0 Q224 -2 226 20 L232 92 Q234 114 212 116 L64 128 Q40 130 38 108 Z" fill="var(--badge-orange)"/>
        <path d="M38 108 Q40 130 64 128 L212 116 Q226 115 231 104 L234 112 Q230 128 212 130 L62 142 Q36 144 34 118 Z" fill="var(--badge-shade)"/>
      </svg>
      <div class="hire-badge__label">Hire Me<br>On</div>
    </div>
  </section>

  <footer class="promo__footer">
    <span class="brand-dot" aria-hidden="true"></span>
    <span class="brand-name">pixelharbor.com</span>
  </footer>
</main>
</body>
</html>
```